Lumora aesthetics offers a range of facial aesthetics treatments by a fully qualified dentist, to a high end crowd. Treatments include antiwrinkle treatment, the use of dermal fillers to provide facial volumisation and rejuvenation and also lip volumisation.
I want a luxurious and bold look. Black background with a bold striking gold logo in the centre possibly incorporating the outline of a face in a subtle yet effective way. I want it to include the work I offer so people will be aware of what they are looking into but not look like there's too much on the card, So it's a clean look.
At the bottom I would like it to say by Dr. Meera Sandhu. Alongside my email address and mobile number.

```html
<!DOCTYPE html>
<html lang="en">
<head>
<meta charset="utf-8">
<title>Lumora Aesthetics – Business Card</title>
<link rel="stylesheet" href="https://fonts.googleapis.com/css2?family=Saira:wght@700&family=Oswald:wght@500&family=Open+Sans:wght@400&display=swap">
<style>
  :root {
    --page-bg: #e9e6e1;
    --card-bg: #232323;
    --gold: #b8913f;
    --gold-label: #c49a45;
    --text-light: #e4e4e4;
    --text-muted: #bdbdbd;
    --accent-fade: rgba(255,255,255,0.05);
  }
  * { margin: 0; padding: 0; box-sizing: border-box; }
  html, body {
    width: 1200px;
    height: 1000px;
    overflow: hidden;
    background: var(--page-bg);
  }
  .business-card {
    position: absolute;
    left: 180px;
    top: 260px;
    width: 840px;
    height: 480px;
    background: var(--card-bg);
    border-radius: 22px;
    overflow: hidden;
    box-shadow: 0 10px 30px rgba(0,0,0,0.25);
  }
  .profile-motif {
    position: absolute;
    right: 40px;
    top: 40px;
    width: 300px;
    height: 320px;
    border-radius: 50% 40% 45% 50%;
    background: radial-gradient(ellipse at 60% 45%, var(--accent-fade), transparent 70%);
  }
  .brand-name {
    position: absolute;
    left: 270px;
    top: 120px;
    font-family: "Saira", sans-serif;
    font-weight: 700;
    font-size: 50px;
    letter-spacing: 1px;
    color: var(--gold);
    text-transform: uppercase;
    white-space: nowrap;
  }
  .practitioner {
    position: absolute;
    left: 70px;
    top: 250px;
  }
  .practitioner-name {
    font-family: "Oswald", sans-serif;
    font-weight: 500;
    font-size: 44px;
    line-height: 1.1;
    color: var(--gold);
    text-transform: uppercase;
    white-space: nowrap;
  }
  .treatment-list {
    list-style: none;
    margin-top: 8px;
    font-family: "Open Sans", sans-serif;
    font-size: 16px;
    line-height: 1.3;
    color: var(--text-light);
  }
  .contact {
    position: absolute;
    left: 480px;
    top: 325px;
    font-family: "Open Sans", sans-serif;
    font-size: 19px;
    line-height: 1.3;
    color: var(--text-muted);
  }
  .address { margin-bottom: 26px; padding-left: 8px; }
  .contact-line { color: var(--text-light); white-space: nowrap; }
  .contact-label { color: var(--gold-label); }
</style>
</head>
<body>
  <div class="business-card">
    <div class="profile-motif" role="img" aria-label="Faint line drawing of a woman's profile with flowing hair"></div>

    <div class="brand-name">Lumora Aesthetics</div>

    <div class="practitioner">
      <div class="practitioner-name">Dr. Meera Sandhu</div>
      <ul class="treatment-list">
        <li>Antiwrinkle Treatment</li>
        <li>Facial Volumisation</li>
        <li>Lip Volumisation</li>
      </ul>
    </div>

    <div class="contact">
      <p class="address">Your Street Address,<br>Singapore, 1234</p>
      <p class="contact-line"><span class="contact-label">Email:</span> yourname@email.com</p>
      <p class="contact-line"><span class="contact-label">Phone:</span> +000 123 456 789</p>
    </div>
  </div>
</body>
</html>
```